The Tress Arbor needs Business Cards

The Tress Arbor is a premier provider of natural hair extensions and wigs. We're looking for a double sided business card that complements our logo and is consistent with the style, look and feel of our logo/image.

```html
<!DOCTYPE html>
<html lang="en">
<head>
<meta charset="utf-8">
<title>The Tress Arbor — Business Cards</title>
<link href="https://fonts.googleapis.com/css2?family=Didact+Gothic&family=Open+Sans:wght@400&display=swap" rel="stylesheet">
<style>
  :root {
    --backdrop: #e9e7e3;
    --card: #ffffff;
    --ink: #262626;
    --gold: #c9a449;
    --muted: #8a7f66;
    --soft: #5b5b5b;
  }
  * { box-sizing: border-box; margin: 0; padding: 0; }
  html, body { width: 1200px; height: 900px; overflow: hidden; }
  body {
    background: var(--backdrop);
    display: flex;
    flex-direction: column;
    align-items: center;
    justify-content: center;
    gap: 40px;
  }
  .card {
    width: 700px;
    height: 400px;
    background: var(--card);
    box-shadow: 0 6px 18px rgba(0,0,0,0.12);
    position: relative;
    overflow: hidden;
  }

  /* brand lockup */
  .brand { display: flex; flex-direction: column; align-items: flex-start; }
  .brand-row { display: flex; align-items: center; gap: 12px; }
  .brand-name {
    font-family: "Didact Gothic", sans-serif;
    font-size: 44px;
    color: var(--ink);
    line-height: 1;
    white-space: nowrap;
  }
  .brand-dot {
    width: 30px; height: 30px;
    border-radius: 50%;
    background: var(--gold);
    flex: none;
  }
  .brand-tagline {
    font-family: "Didact Gothic", sans-serif;
    font-size: 14px;
    letter-spacing: 5px;
    color: var(--muted);
    margin-top: 6px;
    white-space: nowrap;
  }

  /* front */
  .card-front { display: flex; align-items: center; }
  .front-rule {
    position: absolute;
    left: 0; right: 0; top: 50%;
    height: 1.5px;
    background: var(--gold);
  }
  .card-front .brand {
    position: relative;
    margin: 0 auto;
    background: var(--card);
    padding: 0 18px;
  }

  /* back */
  .card-back { padding: 0; }
  .card-back .brand {
    position: absolute;
    left: 36px; top: 190px;
  }
  .card-back .brand-name { font-size: 36px; }
  .card-back .brand-dot { width: 24px; height: 24px; }
  .card-back .brand-tagline { font-size: 12px; letter-spacing: 4px; }
  .back-divider {
    position: absolute;
    left: 402px; top: 28px;
    width: 1.5px; height: 180px;
    background: var(--gold);
  }
  .contact-list {
    position: absolute;
    left: 420px; top: 36px;
    list-style: none;
    display: flex; flex-direction: column; gap: 14px;
  }
  .contact-item, .address {
    display: flex; align-items: center; gap: 10px;
    font-family: "Open Sans", sans-serif;
    font-size: 14px;
    color: var(--soft);
  }
  .icon { width: 18px; height: 18px; flex: none; }
  .address { position: absolute; left: 420px; bottom: 44px; }
</style>
</head>
<body>

  <section class="card card-front">
    <div class="front-rule"></div>
    <div class="brand">
      <div class="brand-row">
        <span class="brand-name">The Tress Arbor</span>
        <span class="brand-dot"></span>
      </div>
      <span class="brand-tagline">Virgin Hair Extensions</span>
    </div>
  </section>

  <section class="card card-back">
    <div class="brand">
      <div class="brand-row">
        <span class="brand-name">The Tress Arbor</span>
        <span class="brand-dot"></span>
      </div>
      <span class="brand-tagline">Virgin Hair Extensions</span>
    </div>

    <div class="back-divider"></div>

    <ul class="contact-list">
      <li class="contact-item">
        <svg class="icon" viewBox="0 0 20 20"><circle cx="10" cy="10" r="10" fill="#c9a449"/><path d="M7 5.5l2 2-1 1.3c.6 1.3 1.6 2.3 2.9 2.9l1.3-1 2 2-1.3 1.5C9.6 14 6 10.4 5.7 7z" fill="#fff"/></svg>
        <span>014 220 5817</span>
      </li>
      <li class="contact-item">
        <svg class="icon" viewBox="0 0 20 20"><circle cx="10" cy="10" r="10" fill="#c9a449"/><path d="M7 5.5l2 2-1 1.3c.6 1.3 1.6 2.3 2.9 2.9l1.3-1 2 2-1.3 1.5C9.6 14 6 10.4 5.7 7z" fill="#fff"/></svg>
        <span>014 220 5818</span>
      </li>
      <li class="contact-item">
        <svg class="icon" viewBox="0 0 20 20"><circle cx="10" cy="10" r="10" fill="#c9a449"/><rect x="5" y="6.5" width="10" height="7" fill="#fff"/><path d="M5 6.5l5 4 5-4" fill="none" stroke="#c9a449" stroke-width="1"/></svg>
        <span>hello@tressarbor.com</span>
      </li>
      <li class="contact-item">
        <svg class="icon" viewBox="0 0 20 20"><circle cx="10" cy="10" r="10" fill="#c9a449"/><circle cx="10" cy="10" r="5" fill="none" stroke="#fff" stroke-width="1.2"/><path d="M5 10h10M10 5c-2 3-2 7 0 10M10 5c2 3 2 7 0 10" fill="none" stroke="#fff" stroke-width="1"/></svg>
        <span>www.tressarbor.com</span>
      </li>
    </ul>

    <div class="address">
      <svg class="icon" viewBox="0 0 20 20"><path d="M10 1.5a6 6 0 0 0-6 6c0 4.5 6 11 6 11s6-6.5 6-11a6 6 0 0 0-6-6z" fill="#c9a449"/><circle cx="10" cy="7.5" r="2.2" fill="#fff"/></svg>
      <span>48 Willow Lane, Greenfield, Ashford 2210</span>
    </div>
  </section>

</body>
</html>
```